Business Card Design

We need a business card design for a Dry cleaners in Brisbane, Australia. We are trying to promote a fresh/clean image consistent with our website. www.quillpresswash.com.au

Looking for a professional neat card that's easy to read.

Target Market(s)

Customers looking for a professional, fresh and clean drycleaners.

Industry/Entity Type

Business

Contact Information for Business Card

See our existing business card. The Fax number (07) 3468 5203 to be removed.

Requirements
Must have
• All the details on current business card less the fax number.
Nice to have
• I like white text on coloured background. Blue works well as we are located near the water...

```html
<!DOCTYPE html>
<html lang="en">
<head>
<meta charset="utf-8">
<title>Quill Press Wash – Business Card</title>
<link rel="stylesheet" href="https://fonts.googleapis.com/css2?family=Lato:wght@400;700&display=swap">
<style>
  :root {
    --backdrop: #e9e7e3;
    --card: #ffffff;
    --card-shade: #eceef0;
    --brand-blue: #5b6db3;
    --accent-orange: #ea6a2e;
    --text-grey: #6d6f78;
    --rule: #8e9ac8;
  }
  * { margin: 0; padding: 0; box-sizing: border-box; }
  html, body {
    width: 1200px;
    height: 600px;
    overflow: hidden;
    background: var(--backdrop);
    font-family: "Lato", Arial, sans-serif;
  }
  .stage {
    width: 1200px;
    height: 600px;
    display: flex;
    align-items: center;
    justify-content: center;
  }
  .card {
    position: relative;
    width: 700px;
    height: 400px;
    border-radius: 22px;
    background: radial-gradient(ellipse at 35% 45%, var(--card) 40%, var(--card-shade) 100%);
    box-shadow: 0 10px 30px rgba(0,0,0,0.12);
  }
  .brand {
    position: absolute;
    left: 60px;
    top: 300px;
    display: flex;
    align-items: center;
    gap: 12px;
    color: var(--brand-blue);
    font-weight: 700;
    font-size: 34px;
    letter-spacing: 0.5px;
  }
  .brand-dot {
    width: 16px;
    height: 16px;
    border-radius: 50%;
    background: var(--brand-blue);
  }
  .divider {
    position: absolute;
    left: 320px;
    top: 292px;
    width: 300px;
    height: 1px;
    background: linear-gradient(90deg, var(--rule), var(--rule) 60%, transparent);
  }
  .contact {
    position: absolute;
    left: 360px;
    top: 50px;
    color: var(--text-grey);
    font-size: 15px;
    line-height: 1.45;
  }
  .contact-name {
    color: var(--accent-orange);
    font-weight: 700;
    font-size: 22px;
    margin-bottom: 6px;
  }
  .contact-address { margin-bottom: 8px; }
  .contact-list { list-style: none; }
  .contact-list li {
    display: flex;
    align-items: center;
    gap: 10px;
  }
  .contact-icon {
    width: 13px;
    height: 13px;
    flex: none;
  }
  .locations {
    position: absolute;
    right: 46px;
    bottom: 40px;
    color: var(--brand-blue);
    font-size: 15px;
  }
</style>
</head>
<body>
<main class="stage">
  <section class="card">
    <div class="contact">
      <p class="contact-name">Maren Collis</p>
      <p class="contact-address">18 Colvin Rd<br>Harlow Qld 4172</p>
      <ul class="contact-list">
        <li>
          <svg class="contact-icon" viewBox="0 0 13 13"><rect x="3" y="0.5" width="7" height="12" rx="1.5" fill="var(--accent-orange)"/><rect x="4.5" y="2" width="4" height="7" fill="#fff"/></svg>
          0412 508 274
        </li>
        <li>
          <svg class="contact-icon" viewBox="0 0 13 13"><rect x="0.5" y="0.5" width="12" height="12" rx="1.5" fill="none" stroke="var(--accent-orange)"/><path d="M3.5 3.5c0 3.5 2.5 6 6 6l0.8-1.6-1.8-1-0.9 0.9c-1-0.5-1.9-1.4-2.4-2.4l0.9-0.9-1-1.8z" fill="var(--accent-orange)"/></svg>
          (07) 3251 0846
        </li>
        <li>
          <svg class="contact-icon" viewBox="0 0 13 13"><rect x="0.5" y="2.5" width="12" height="8" fill="var(--accent-orange)"/><path d="M0.5 2.5l6 4.5 6-4.5" fill="none" stroke="#fff"/></svg>
          maren@quillpresswash.com.au
        </li>
        <li>
          <svg class="contact-icon" viewBox="0 0 13 13"><rect x="0.5" y="0.5" width="12" height="12" rx="1.5" fill="none" stroke="var(--accent-orange)"/><circle cx="6.5" cy="6.5" r="3.5" fill="none" stroke="var(--accent-orange)"/><path d="M3 6.5h7M6.5 3v7" stroke="var(--accent-orange)" stroke-width="0.8"/></svg>
          www.quillpresswash.com.au
        </li>
      </ul>
    </div>

    <div class="divider"></div>

    <div class="brand"><span class="brand-dot"></span>Quill Press Wash</div>

    <p class="locations">Harlow | Brenmore | Kestrel Pt</p>
  </section>
</main>
</body>
</html>
```